Honey Vinegar Gift Set/Sampler Pack packaging Design Needed

We need packaging designed for our three pack vinegar holder. there are 5 possible vinegars going into this package, so the design needs to work for any selection.

The three pack will hold three 100ml vinegar bottles. The bottles are Tarne bottles.
The 5 vinegars that might go into this package are:
- Honey vinegar
- Honey garlic vinegar
- Honey apple cider vinegar
- Honey Raspberry vinegar
- Buckwheat Honey Malt Vinegar

Target Market(s)

Foodies, local food enthusiast, gourmet food

Industry/Entity Type

Work

Colors

Designer to choose colors to be used in the design.

Requirements
Must have
• same colour schemes as current labels. Same font, design to flow from bottle labels to packaging

```html
<!DOCTYPE html>
<html lang="en">
<head>
<meta charset="utf-8">
<title>Honey Vinegar Taster's Pack – Carton Dieline</title>
<link href="https://fonts.googleapis.com/css2?family=Oswald:wght@300;400;500&family=Roboto+Slab:wght@700&family=Caveat:wght@600&display=swap" rel="stylesheet">
<style>
  :root {
    --paper: #ffffff;
    --pattern: #f1f1f1;
    --honey: #fbc263;
    --honey-light: #fdd9a3;
    --orange: #f47b2a;
    --brown: #5b2b1c;
    --gold-a: #e9d27a;
    --gold-b: #b78d2c;
    --ink: #1c1c1c;
    --window: #555555;
    --cut: #222222;
    --fold: #2aa3e0;
    --amber-a: #f5b23a;
    --amber-b: #c9780c;
  }
  * { margin: 0; padding: 0; box-sizing: border-box; }
  html, body { width: 1101px; height: 1200px; overflow: hidden; background: var(--paper); }
  .canvas { position: relative; width: 1101px; height: 1200px; font-family: "Oswald", sans-serif; }
  .abs { position: absolute; }

  .pattern { background: var(--pattern); }
  .gold-band { background: linear-gradient(100deg, var(--gold-b), var(--gold-a) 35%, #f4e7a8 55%, var(--gold-b)); }
  .brush-band { background: linear-gradient(180deg, #3a3a3a, var(--ink)); }
  .tagline { font-family: "Caveat", cursive; font-size: 21px; color: var(--ink); text-align: center; width: 384px; }
  .honey-field { background: var(--honey); border-radius: 0 0 40% 60% / 0 0 14px 20px; }
  .label-pill { background: var(--honey-light); border-radius: 30px; }
  .brand-box { background: var(--orange); color: #fff; font-family: "Oswald", sans-serif; font-weight: 400; display: flex; align-items: center; justify-content: center; gap: 6px; text-align: center; line-height: 1.05; border: 1px solid #ffd2a8; }
  .brand-dot { width: 14px; height: 14px; border-radius: 50%; background: #fff; flex: none; }
  .pack-frame { border: 1px solid var(--brown); border-radius: 8px; }
  .side-word { font-family: "Roboto Slab", serif; font-weight: 700; font-size: 15px; color: var(--brown); letter-spacing: .5px; writing-mode: vertical-rl; white-space: nowrap; text-align: center; }
  .side-word.up { transform: rotate(180deg); }
  .title { font-family: "Oswald", sans-serif; font-weight: 300; font-size: 60px; color: var(--brown); letter-spacing: -1px; line-height: 1; white-space: nowrap; width: 332px; display: flex; justify-content: center; transform: scale(0.82, 1.1); transform-origin: center top; }
  .rule { height: 1px; background: var(--brown); }
  .subtitle { font-family: "Oswald", sans-serif; font-weight: 500; font-size: 12px; color: var(--brown); text-align: center; width: 332px; white-space: nowrap; }
  .bottle-window { background: var(--window); border-radius: 34px 34px 0 0; }
  .amber-pour { background: linear-gradient(170deg, var(--amber-a), #e59a1c 45%, var(--amber-b)); }
  .volume-pill { background: #fff; border-radius: 14px; font-family: "Oswald", sans-serif; font-size: 12px; color: var(--ink); display: flex; align-items: center; justify-content: center; }
  .about { font-family: "Oswald", sans-serif; font-weight: 300; font-size: 13.3px; line-height: 17.6px; color: var(--ink); text-align: justify; width: 326px; }
  .about p + p { margin-top: 16px; }
  .taste-title { font-family: "Oswald", sans-serif; font-weight: 300; font-size: 13.3px; color: var(--ink); }
  .flavour { width: 78px; text-align: center; }
  .flavour-art { width: 48px; height: 48px; border-radius: 50%; margin: 0 auto 8px; }
  .flavour-name { font-family: "Oswald", sans-serif; font-weight: 300; font-size: 10.5px; line-height: 13px; }
  .learn { font-family: "Oswald", sans-serif; font-weight: 400; font-size: 14px; color: var(--ink); text-align: right; width: 220px; }
  .url { font-family: "Oswald", sans-serif; font-weight: 400; font-size: 14px; color: var(--orange); text-align: right; width: 220px; }
  .dieline { position: absolute; inset: 0; }
  .reg-dot { width: 18px; height: 18px; border-radius: 50%; background: var(--ink); }
</style>
</head>
<body>
<main class="canvas">

  <div class="abs pattern" style="left:0;top:276px;width:196px;height:924px" role="img" aria-label="Light grey line pattern of apples, raspberries, garlic, wheat, bees and honeycomb"></div>
  <div class="abs pattern" style="left:580px;top:260px;width:128px;height:940px" role="img" aria-label="Light grey line pattern of apples, raspberries, garlic, wheat, bees and honeycomb"></div>
  <div class="abs pattern" style="left:196px;top:590px;width:384px;height:380px" role="img" aria-label="Light grey line pattern of apples, raspberries, garlic, wheat, bees and honeycomb"></div>
  <div class="abs pattern" style="left:708px;top:590px;width:384px;height:380px" role="img" aria-label="Light grey line pattern of apples, raspberries, garlic, wheat, bees and honeycomb"></div>
  <div class="abs pattern" style="left:708px;top:1100px;width:393px;height:100px" role="img" aria-label="Light grey line pattern of fruit and bees"></div>

  <div class="abs brand-box" style="left:328px;top:80px;width:119px;height:48px;font-size:13px">
    <span class="brand-dot"></span><span>MEADOWLINE<br>APIARY</span>
  </div>

  <section class="front">
    <div class="abs honey-field" style="left:196px;top:260px;width:384px;height:342px"></div>
    <div class="abs gold-band" style="left:196px;top:260px;width:384px;height:44px" role="img" aria-label="Gold foil texture band"></div>
    <div class="abs brush-band" style="left:196px;top:302px;width:384px;height:24px"></div>
    <div class="abs tagline" style="left:196px;top:268px">naturally fermented</div>
    <div class="abs label-pill" style="left:300px;top:338px;width:176px;height:60px"></div>
    <div class="abs pack-frame" style="left:222px;top:426px;width:332px;height:152px"></div>
    <div class="abs side-word" style="left:228px;top:432px;height:142px">TASTER'S PACK</div>
    <div class="abs side-word up" style="left:532px;top:432px;height:142px">TASTER'S PACK</div>
    <div class="abs brand-box" style="left:318px;top:406px;width:140px;height:56px;font-size:15px">
      <span class="brand-dot"></span><span>MEADOWLINE<br>APIARY</span>
    </div>
    <div class="abs title" style="left:222px;top:474px">HONEY VINEGAR</div>
    <div class="abs rule" style="left:266px;top:550px;width:244px"></div>
    <div class="abs subtitle" style="left:222px;top:555px">LOCAL, SMALL BATCH ARTISAN VINEGARS</div>

    <div class="abs amber-pour" style="left:192px;top:964px;width:392px;height:136px" role="img" aria-label="Pouring golden honey vinegar with line-drawn flower and wheat"></div>
    <div class="abs bottle-window" style="left:226px;top:692px;width:68px;height:318px"></div>
    <div class="abs bottle-window" style="left:354px;top:692px;width:68px;height:318px"></div>
    <div class="abs bottle-window" style="left:482px;top:692px;width:68px;height:318px"></div>
    <div class="abs volume-pill" style="left:336px;top:1034px;width:104px;height:26px">300 ML (3 X 100 ML)</div>
  </section>

  <div class="abs brand-box" style="left:92px;top:686px;width:80px;height:200px;font-size:20px;writing-mode:vertical-rl;transform:rotate(180deg);">
    <span class="brand-dot"></span><span>MEADOWLINE APIARY</span>
  </div>
  <div class="abs brand-box" style="left:606px;top:686px;width:80px;height:200px;font-size:20px;writing-mode:vertical-rl;transform:rotate(180deg);">
    <span class="brand-dot"></span><span>MEADOWLINE APIARY</span>
  </div>

  <section class="back">
    <div class="abs honey-field" style="left:708px;top:260px;width:384px;height:342px"></div>
    <div class="abs gold-band" style="left:708px;top:260px;width:384px;height:44px" role="img" aria-label="Gold foil texture band"></div>
    <div class="abs brush-band" style="left:708px;top:302px;width:384px;height:24px"></div>
    <div class="abs tagline" style="left:708px;top:268px">naturally fermented</div>
    <div class="abs label-pill" style="left:813px;top:338px;width:176px;height:60px"></div>
    <div class="abs pack-frame" style="left:735px;top:426px;width:332px;height:152px"></div>
    <div class="abs side-word" style="left:741px;top:432px;height:142px">TASTER'S PACK</div>
    <div class="abs side-word up" style="left:1045px;top:432px;height:142px">TASTER'S PACK</div>
    <div class="abs brand-box" style="left:831px;top:406px;width:140px;height:56px;font-size:15px">
      <span class="brand-dot"></span><span>MEADOWLINE<br>APIARY</span>
    </div>
    <div class="abs title" style="left:735px;top:474px">HONEY VINEGAR</div>
    <div class="abs rule" style="left:779px;top:550px;width:244px"></div>
    <div class="abs subtitle" style="left:735px;top:555px">LOCAL, SMALL BATCH ARTISAN VINEGARS</div>

    <div class="abs about" style="left:737px;top:630px">
      <p>Meadowline Apiary is a family run beekeeping operation located in Millbrook, Ontario. Our honey bees are located throughout the Greater Toronto Area, pollinating the local flora.</p>
      <p>Following a traditional static fermentation method, our vinegar is made in small batches without the use of preservatives or sulfites. Followed with six months of aging, the resulting vinegars are smooth and balanced.</p>
    </div>
    <div class="abs taste-title" style="left:737px;top:788px">Taste them all</div>

    <div class="abs flavour" style="left:702px;top:844px">
      <div class="flavour-art" style="background:#f2b62a" role="img" aria-label="Honeycomb and bee illustration"></div>
      <div class="flavour-name" style="color:#e6a016">Honey<br>Vinegar</div>
    </div>
    <div class="abs flavour" style="left:781px;top:844px">
      <div class="flavour-art" style="background:#e9853a" role="img" aria-label="Garlic bulb illustration"></div>
      <div class="flavour-name" style="color:#e07a1f">Honey Vinegar<br>with Garlic</div>
    </div>
    <div class="abs flavour" style="left:859px;top:844px">
      <div class="flavour-art" style="background:#a6d12a" role="img" aria-label="Green apple illustration"></div>
      <div class="flavour-name" style="color:#7fa51a">Honey Apple<br>Cider Vinegar</div>
    </div>
    <div class="abs flavour" style="left:937px;top:844px">
      <div class="flavour-art" style="background:#e02a5c" role="img" aria-label="Raspberry illustration"></div>
      <div class="flavour-name" style="color:#c81c46">Honey<br>Raspberry Vinegar</div>
    </div>
    <div class="abs flavour" style="left:1012px;top:844px">
      <div class="flavour-art" style="background:#5ec4d4" role="img" aria-label="Buckwheat flower and wheat illustration"></div>
      <div class="flavour-name" style="color:#17808f">Buckwheat Honey<br>Malt Vinegar</div>
    </div>

    <div class="abs amber-pour" style="left:704px;top:968px;width:388px;height:132px" role="img" aria-label="Pouring golden honey vinegar with line-drawn flower and wheat"></div>
    <div class="abs learn" style="left:852px;top:972px">Learn more at</div>
    <div class="abs url" style="left:852px;top:990px">www.meadowlineapiary.com</div>
  </section>

  <svg class="dieline" width="1101" height="1200" viewBox="0 0 1101 1200" fill="none" stroke-width="1">
    <g class="cut-lines" stroke="var(--cut)">
      <path d="M196 260 L196 240 C196 150 250 75 310 62 L310 30 C310 16 318 10 330 10 L450 10 C462 10 470 16 470 30 L470 62 C530 75 580 150 580 240 L580 260"/>
      <rect x="300" y="138" width="176" height="58" rx="29"/>
      <rect x="98" y="376" width="68" height="176" rx="34"/>
      <rect x="610" y="376" width="68" height="176" rx="34"/>
      <path d="M0 276 L70 280 L150 276 L196 266"/>
      <path d="M580 270 L640 282 L708 282"/>
      <path d="M10 276 L10 1080 L70 1100 L120 1140 L130 1188 L196 1188 L196 1100"/>
      <path d="M196 1100 L230 1100 L250 1120 L260 1150 L260 1180 L270 1188 L500 1188 L512 1180 L512 1150 L525 1120 L545 1100 L580 1100"/>
      <path d="M580 1100 L580 1188 L708 1188 L708 1100"/>
      <path d="M708 1188 L750 1188 L750 1150 L1060 1150 L1060 1188 L1092 1188 L1092 1100"/>
    </g>
    <g class="fold-lines" stroke="var(--fold)">
      <path d="M70 282 L70 1086 L196 1086"/>
      <path d="M132 282 L132 376 M132 552 L70 614 M166 552 L196 600"/>
      <path d="M580 1086 L708 1086 M708 282 L708 1100 M644 282 L644 376 M610 552 L580 614 M678 552 L708 600"/>
    </g>
  </svg>

  <div class="abs reg-dot" style="left:0;top:0"></div>
  <div class="abs reg-dot" style="left:1082px;top:0"></div>
  <div class="abs reg-dot" style="left:0;top:1182px"></div>
  <div class="abs reg-dot" style="left:1082px;top:1182px"></div>
</main>
</body>
</html>
```